New River III Precinct 6x11 GOTV postcard

We require BOTH persuasive copy and high-impact layout for an oversized 6x11 political mailer. This might be one person, but it likely requires a specialized "creative team." of an experienced political strategist copywriter PLUS a graphic designer - so the words fit the exact layout block, and the visuals reinforce the psychological punch of the headline.

The goal is to remove all excuses a targeted audience of ~900 registered Democratic + ~1800 Unaffiliated voters in our precinct - have for not voting.

I need to be able to work by phone / online chat to iterate designs
I need to own the design in the top couple of software outputs that any printer service will require.

I want to experiment with very subtle background images as follows:
- Front of postcard that conveys "CHANGE" of not just seasons - but of encouraging change of precinct voter representation - so anything about fall foliage / conveyance of change tie-in is worthy of considering
- Back of postcard - any Appalachian long rage mountain view that includes 5-7 layers of hills in the distance.
Some photos as samples to consider.

Target Market(s)

~2,700 registered Democrats and Unaffiliated voters

Requirements
Must have
• We require BOTH persuasive copy and high-impact layout for an oversized 6x11 political mailer. This might be one person, but it likely requires a specialized "creative team." of an experienced political strategist copywriter PLUS a graphic designer - so the words fit the exact layout block, and the visuals reinforce the psychological punch of the headline
Nice to have
• subtle background photos

```html
<!DOCTYPE html>
<html lang="en">
<head>
<meta charset="utf-8">
<title>New River Precinct GOTV Postcard</title>
<link rel="stylesheet" href="https://fonts.googleapis.com/css2?family=Oswald:wght@400;500;600;700&family=Roboto+Condensed:wght@400;500;700&display=swap">
<style>
  :root {
    --navy: #1c2f5a;
    --navy-deep: #142449;
    --red: #a3202b;
    --gold: #d49a2a;
    --paper: #f7f2ea;
    --ink: #333842;
    --rule: #9aa3b5;
    --stage: #e8e5e0;
  }
  * { box-sizing: border-box; margin: 0; padding: 0; }
  html, body { width: 1200px; height: 800px; overflow: hidden; }
  body { background: var(--stage); font-family: "Roboto Condensed", Arial, sans-serif; color: var(--ink); position: relative; }

  .postcard { position: absolute; left: 250px; width: 700px; height: 382px; overflow: hidden; box-shadow: 0 2px 8px rgba(0,0,0,.15); }
  .postcard--back { top: 10px; background: var(--paper); }
  .postcard--front { top: 404px; background: #eef0f4; }

  .bg-photo { position: absolute; inset: 0; }
  .back-photo { right: auto; width: 400px; background: radial-gradient(ellipse at 20% 40%, rgba(236,196,160,.35), transparent 60%), linear-gradient(180deg, rgba(240,215,190,.25), rgba(246,238,228,.1)); }
  .front-photo { background: linear-gradient(180deg, #dfe4ee 0%, #eef0f4 45%, #dde3ec 75%, #e9ecf1 100%); }

  .headline { font-family: "Oswald", Arial, sans-serif; font-weight: 600; letter-spacing: .5px; line-height: 1; text-transform: uppercase; }

  /* Back side */
  .back-title { position: absolute; left: 28px; top: 20px; font-size: 42px; color: var(--navy); }
  .back-title .accent { color: var(--gold); }
  .title-rule { position: absolute; left: 28px; top: 68px; width: 310px; height: 12px; }
  .back-copy { position: absolute; left: 28px; top: 86px; width: 345px; font-size: 9px; line-height: 1.32; }
  .back-copy p { margin-bottom: 6px; }
  .back-copy strong { color: var(--navy); }
  .callout { font-family: "Oswald", Arial, sans-serif; font-weight: 500; color: var(--red); font-size: 10.5px; text-transform: uppercase; border-bottom: 1px solid var(--gold); padding-bottom: 3px; margin-bottom: 6px; }
  .point { display: flex; align-items: center; gap: 8px; margin-bottom: 5px; }
  .point svg { flex: 0 0 24px; }
  .point .red { color: var(--red); font-weight: 700; text-transform: uppercase; }

  .info-grid { position: absolute; left: 22px; top: 290px; width: 380px; height: 80px; display: grid; grid-template-columns: 1fr 1fr; border: 1px solid var(--rule); background: rgba(255,255,255,.7); }
  .info-cell { display: flex; align-items: center; gap: 7px; padding: 4px 8px; border-right: 1px solid var(--rule); border-bottom: 1px solid var(--rule); font-family: "Oswald", Arial, sans-serif; font-size: 7.5px; text-transform: uppercase; color: var(--navy); line-height: 1.25; }
  .info-cell:nth-child(even) { border-right: none; }
  .info-cell:nth-child(n+3) { border-bottom: none; }
  .info-cell svg { flex: 0 0 16px; }
  .info-cell small { display: block; font-size: 6.5px; color: var(--ink); margin-top: 2px; }

  .stamp-box { position: absolute; right: 40px; top: 24px; width: 72px; height: 82px; border: 1px solid var(--navy); }
  .address-box { position: absolute; left: 420px; top: 150px; width: 222px; height: 112px; border: 1px solid var(--navy); }

  /* Front side */
  .flag-field { position: absolute; top: 0; right: 0; width: 150px; height: 100%; clip-path: polygon(22% 0, 100% 0, 100% 100%, 0 100%, 6% 60%); background: linear-gradient(180deg, var(--navy-deep) 0%, var(--navy) 38%, #c9cdd8 50%, var(--red) 62%, #8e1b25 100%); }
  .front-title { position: absolute; left: 60px; top: 16px; font-size: 47px; color: var(--navy); font-weight: 700; }
  .front-title .accent { color: var(--red); }
  .pain-band { position: absolute; left: 40px; top: 78px; width: 530px; height: 38px; background: var(--navy); text-align: center; padding-top: 4px; }
  .pain-band .lead { font-family: "Oswald", Arial, sans-serif; font-size: 12px; color: var(--gold); text-transform: uppercase; }
  .pain-band .sub { font-size: 7.5px; color: #fff; margin-top: 1px; }

  .issues { position: absolute; top: 126px; }
  .issues--left { left: 36px; width: 205px; }
  .issues--mid { left: 248px; width: 205px; }
  .issue { display: flex; gap: 7px; margin-bottom: 7px; }
  .issue svg { flex: 0 0 20px; margin-top: 2px; }
  .issue h3 { font-family: "Oswald", Arial, sans-serif; font-weight: 500; font-size: 8.5px; color: var(--red); text-transform: uppercase; }
  .issue p { font-size: 6.8px; line-height: 1.3; color: var(--ink); }

  .ballot { position: absolute; left: 462px; top: 124px; width: 172px; height: 222px; background: rgba(255,255,255,.88); border: 1px solid var(--rule); border-radius: 3px; }
  .ballot h2 { background: var(--navy); color: var(--gold); font-family: "Oswald", Arial, sans-serif; font-weight: 500; font-size: 10.5px; line-height: 1.1; padding: 5px 9px; text-transform: uppercase; }
  .ballot dl { padding: 5px 8px; display: grid; grid-template-columns: 1fr auto; row-gap: 3.5px; column-gap: 4px; font-family: "Oswald", Arial, sans-serif; font-size: 6.5px; text-transform: uppercase; }
  .ballot dt { color: var(--navy-deep); }
  .ballot dd { color: var(--red); align-self: end; }

  .front-band { position: absolute; left: 26px; top: 354px; width: 535px; height: 17px; background: var(--navy); color: #fff; font-family: "Oswald", Arial, sans-serif; font-size: 9.5px; text-transform: uppercase; display: flex; justify-content: center; align-items: center; gap: 7px; }
  .front-band .star { color: var(--gold); }
</style>
</head>
<body>

<section class="postcard postcard--back" aria-label="Postcard back">
  <div class="bg-photo back-photo" role="img" aria-label="Faint layered Appalachian mountain view in warm autumn tones"></div>

  <h1 class="headline back-title">It's time for <span class="accent">Change</span></h1>
  <svg class="title-rule" viewBox="0 0 310 12" aria-hidden="true">
    <line x1="0" y1="3" x2="310" y2="3" stroke="#d49a2a" stroke-width="1"/>
    <polygon points="155,3 157,8 162,8 158,11 160,16 155,13 150,16 152,11 148,8 153,8" fill="#1c2f5a" transform="scale(1,0.75)"/>
  </svg>

  <div class="back-copy">
    <p>We live in a representative democracy. We expect our representatives will exercise independent thinking and support policies and legislation that don't harm us - and that reflect the <strong>MAJORITY VIEWS</strong> of precinct citizens.</p>
    <p>But our current representatives <strong>HAVE STOPPED LISTENING</strong> - they are now bringing harmful policies straight to Watauga County.</p>
    <div class="callout">It's time to hold them accountable and vote them out.</div>
    <div class="point">
      <svg width="24" height="24" viewBox="0 0 24 24" aria-hidden="true"><circle cx="12" cy="12" r="12" fill="#1c2f5a"/><circle cx="12" cy="9" r="2.5" fill="#fff"/><circle cx="7" cy="11" r="2" fill="#fff"/><circle cx="17" cy="11" r="2" fill="#fff"/><path d="M7 17a5 4 0 0 1 10 0z" fill="#fff"/></svg>
      <span>Make no mistake: in 2026, every election is partisan.<br>Even Judicial seats are now tied directly to state platforms.</span>
    </div>
    <div class="point">
      <svg width="24" height="24" viewBox="0 0 24 24" aria-hidden="true"><circle cx="12" cy="12" r="11" fill="none" stroke="#1c2f5a" stroke-width="1.5"/><path d="M6 10h3l7-4v12l-7-4H6z" fill="#1c2f5a"/></svg>
      <span>Any candidate who refuses to publicly condemn Raleigh's gerrymandered overreach into <strong>Watauga politics</strong> or <strong>refuses to fight funding cuts</strong> for our <strong>healthcare, education, and environmental justice</strong> - is actively supporting these harmful policies.</span>
    </div>
    <div class="point">
      <svg width="24" height="24" viewBox="0 0 24 24" aria-hidden="true"><path d="M12 2l8 3v6c0 5-3.5 9-8 11-4.5-2-8-6-8-11V5z" fill="#1c2f5a"/><path d="M8 12l3 3 5-6" stroke="#fff" stroke-width="2" fill="none"/></svg>
      <span>They are hoping their silence fools you.<br><span class="red">Don't be fooled. This November, vote for change.</span></span>
    </div>
  </div>

  <div class="info-grid">
    <div class="info-cell">
      <svg width="16" height="16" viewBox="0 0 16 16" aria-hidden="true"><path d="M8 1a5 5 0 0 1 5 5c0 4-5 9-5 9S3 10 3 6a5 5 0 0 1 5-5z" fill="#d49a2a"/><circle cx="8" cy="6" r="2" fill="#fff"/></svg>
      <div>You are a registered voter<br>in Watauga County<small>You reside in precinct: New River II</small></div>
    </div>
    <div class="info-cell">
      <svg width="16" height="16" viewBox="0 0 16 16" aria-hidden="true"><rect x="2" y="3" width="12" height="11" rx="1" fill="none" stroke="#d49a2a" stroke-width="1.5"/><line x1="2" y1="6.5" x2="14" y2="6.5" stroke="#d49a2a" stroke-width="1.5"/></svg>
      <div>Early voting starts on:</div>
    </div>
    <div class="info-cell">
      <svg width="16" height="16" viewBox="0 0 16 16" aria-hidden="true"><path d="M2 13V7l6-4 6 4v6z" fill="#d49a2a"/><rect x="6" y="9" width="4" height="4" fill="#fff"/></svg>
      <div>Your polling places<br>available to you are:<small>Location: 2, 3</small></div>
    </div>
    <div class="info-cell">
      <svg width="16" height="16" viewBox="0 0 16 16" aria-hidden="true"><rect x="1.5" y="3.5" width="13" height="9" fill="none" stroke="#d49a2a" stroke-width="1.5"/><path d="M1.5 3.5l6.5 5 6.5-5" fill="none" stroke="#d49a2a" stroke-width="1.5"/></svg>
      <div>Deadline to apply for<br>mail-in ballots:<small>Know the rules to ensure mail-in ballot counts</small></div>
    </div>
  </div>

  <div class="stamp-box" aria-label="Postage area"></div>
  <div class="address-box" aria-label="Address area"></div>
</section>

<section class="postcard postcard--front" aria-label="Postcard front">
  <div class="bg-photo front-photo" role="img" aria-label="Soft pale sky over distant layered mountain ridges"></div>
  <div class="flag-field" role="img" aria-label="Waving American flag"></div>

  <h1 class="headline front-title">Vote for <span class="accent">New Representation</span></h1>

  <div class="pain-band">
    <div class="lead">Local pain – thanks to current representatives –</div>
    <div class="sub">and sadly, to avoid accountability, they've cleverly delayed many / most impacts until AFTER the 2026 election.</div>
  </div>

  <div class="issues issues--left">
    <div class="issue">
      <svg width="20" height="20" viewBox="0 0 20 20" aria-hidden="true"><circle cx="7" cy="6" r="3" fill="#1c2f5a"/><path d="M2 17a5 5 0 0 1 10 0z" fill="#1c2f5a"/><circle cx="15" cy="13" r="4" fill="#1c2f5a"/><text x="15" y="15.5" font-size="6" fill="#fff" text-anchor="middle" font-family="Arial">$</text></svg>
      <div><h3>Family Budget –</h3><p>exploded costs for everything: groceries, gas, car insurance, rent.</p></div>
    </div>
    <div class="issue">
      <svg width="20" height="20" viewBox="0 0 20 20" aria-hidden="true"><path d="M10 18S2 12 2 7a4 4 0 0 1 8-1 4 4 0 0 1 8 1c0 5-8 11-8 11z" fill="#1c2f5a"/><path d="M10 6v7M6.5 9.5h7" stroke="#fff" stroke-width="1.8"/></svg>
      <div><h3>Health –</h3><p>expired subsidies, tax credits mean families in NC will lose coverage or pay more. 50% cuts to hospitals, mental health facilities; rural facilities at risk.</p></div>
    </div>
    <div class="issue">
      <svg width="20" height="20" viewBox="0 0 20 20" aria-hidden="true"><circle cx="10" cy="6" r="3.5" fill="none" stroke="#1c2f5a" stroke-width="1.6"/><path d="M10 9.5V14M8 12h4" stroke="#1c2f5a" stroke-width="1.6"/><path d="M2 12c2 4 5 6 8 6s6-2 8-6" fill="none" stroke="#1c2f5a" stroke-width="1.6"/></svg>
      <div><h3>Reproductive Rights –</h3><p>Government authoritarian intrusion – censure women's rights.</p></div>
    </div>
    <div class="issue">
      <svg width="20" height="20" viewBox="0 0 20 20" aria-hidden="true"><path d="M10 1l8 3v6c0 4.5-3.5 8-8 9.5C5.5 18 2 14.5 2 10V4z" fill="#1c2f5a"/><path d="M8 5v9M12 5v9M7 5v3a1 1 0 0 0 2 0" stroke="#fff" stroke-width="1.2" fill="none"/></svg>
      <div><h3>Food Security –</h3><p>Weaponized hunger – cuts to SNAP; school meals cut; additional work requirements.</p></div>
    </div>
    <div class="issue">
      <svg width="20" height="20" viewBox="0 0 20 20" aria-hidden="true"><path d="M2 4c3-1 6-1 8 1v12c-2-2-5-2-8-1zM18 4c-3-1-6-1-8 1v12c2-2 5-2 8-1z" fill="none" stroke="#1c2f5a" stroke-width="1.8"/></svg>
      <div><h3>Education –</h3><p>Watauga $2.2mm shortfall personnel cuts, freezes in hiring, teacher training. Abandoning civil rights of Special Ed students to HHS and DOL.</p></div>
    </div>
  </div>

  <div class="issues issues--mid">
    <div class="issue">
      <svg width="20" height="20" viewBox="0 0 20 20" aria-hidden="true"><path d="M2 10L10 3l8 7h-2v7H4v-7z" fill="#1c2f5a"/><rect x="8" y="12" width="4" height="5" fill="#fff"/></svg>
      <div><h3>Housing –</h3><p>~25% of renters are spending over 50% of income on rent. Especially bad locally; predatory leasing terms and skyrocketing rents. Proposed legislation is transforming HUD with the goal of getting rid of Section 8 housing that cares for vulnerable populations.</p></div>
    </div>
    <div class="issue">
      <svg width="20" height="20" viewBox="0 0 20 20" aria-hidden="true"><circle cx="10" cy="10" r="8.5" fill="none" stroke="#1c2f5a" stroke-width="1.6"/><path d="M11 3L6 11h4l-1 6 5-8h-4z" fill="#1c2f5a"/></svg>
      <div><h3>Energy –</h3><p>In 2022 Boone achieved 100% renewable energy in town buildings; this is now being destroyed by repeal of renewable energy project funding. Ridge State Innovation District prepares renewable workforce technologies – all this is now in limbo.</p></div>
    </div>
    <div class="issue">
      <svg width="20" height="20" viewBox="0 0 20 20" aria-hidden="true"><circle cx="10" cy="10" r="8.5" fill="none" stroke="#1c2f5a" stroke-width="1.6"/><path d="M1.5 10h17M10 1.5c3 3 3 14 0 17M10 1.5c-3 3-3 14 0 17" fill="none" stroke="#1c2f5a" stroke-width="1.2"/></svg>
      <div><h3>Environment –</h3><p>Reduced protections from coal ash pond leaks threaten public health. Corporations not held responsible for damage; public picks up the tab. Environmental Justice enforcement no longer a priority. Logging in Watauga with no public oversight. It's the "haz-mat" model: do nothing, wait for catastrophe, then fix it.</p></div>
    </div>
  </div>

  <aside class="ballot">
    <h2>Sample Ballot<br>Recommendations</h2>
    <dl>
      <dt>US Senate</dt><dd>- Dana Whitfield</dd>
      <dt>US House – District 5</dt><dd>- Marcus Ellery</dd>
      <dt>Reqmt to show ID for<br>voters not in person</dt><dd>- No</dd>
      <dt>State Senate District 47</dt><dd>- Paul Brannock</dd>
      <dt>House of Rep's<br>District 93</dt><dd>- Greta Lindqvist</dd>
      <dt>NC Supreme Court</dt><dd>- Rosa Tremont</dd>
      <dt>NC Court of Appeals –<br>Seat 1</dt><dd>- Neil Castellan</dd>
      <dt>NC Court of Appeals –<br>Seat 2</dt><dd>- Owen Radley</dd>
      <dt>NC Court of Appeals –<br>Seat 3</dt><dd>- Lena Morrow</dd>
    </dl>
  </aside>

  <div class="front-band">
    <span>Your Community</span><span class="star">★</span>
    <span>Your Voice</span><span class="star">★</span>
    <span>Your Vote</span><span class="star">★</span>
    <span>This November, Vote for New</span>
  </div>
</section>

</body>
</html>
```